Business card design for crowd sourced review site.

I need a business card magnet design for an online, crowd-sourced, restaurant review site strictly for Kosher restaurants.
It is similar to RoamLedger but catering to a very particular crowd.
The markets it will be distributed in are flooded with business card fridge magnets so this needs to be eye-catching and unique. The Business name is PlateMarks
The website isnt finished but you can see the basic setup here
http://restaurant.vintrello.com/

The second image i included is another logo design I liked and was thinking about using and decided I will probably also make a SECOND custom cut business card in the shape of that icon. Bonus if you can throw that in also.

Target Market(s)

Jewish consumers aged 20-35

Industry/Entity Type

Business

Contact Information for Business Card

see description.
Design should not be too crowded and should in eye-catching. Will mainly be used as fridge magnets.

Requirements
Must have
• Website address. logo.
Nice to have
• tagline. (The Definitive guide to kosher dining for the Kosher consumer)
• Im not a professional but I personally think the color blue goes along with this concept. ill leave it to you to decide.
Should not have
• any religious symbols.

```html
<!DOCTYPE html>
<html lang="en">
<head>
<meta charset="utf-8">
<title>PlateMarks Business Card</title>
<link rel="stylesheet" href="https://fonts.googleapis.com/css2?family=Montserrat:wght@400;500;600;700&display=swap">
<style>
  :root {
    --stage: #2b2b2b;
    --card-black: #0b0b0b;
    --brand-red: #e03a27;
    --ink: #111111;
    --paper: #ffffff;
    --muted: #3a1410;
  }
  * { box-sizing: border-box; margin: 0; padding: 0; }
  html, body { width: 1200px; height: 1000px; overflow: hidden; }
  body {
    background: var(--stage);
    font-family: "Montserrat", Arial, sans-serif;
    display: flex;
    flex-direction: column;
    align-items: center;
    justify-content: center;
    gap: 60px;
  }
  .card {
    position: relative;
    width: 735px;
    height: 420px;
    border-radius: 22px;
    overflow: hidden;
  }
  /* Front */
  .card-front { background: var(--card-black); }
  .front-wordmark {
    position: absolute;
    left: 0; right: 0; top: 160px;
    text-align: center;
    color: var(--paper);
    font-weight: 700;
    font-size: 64px;
    letter-spacing: 1px;
  }
  .front-tagline {
    position: absolute;
    left: 0; right: 0; bottom: 34px;
    text-align: center;
    color: var(--brand-red);
    font-weight: 500;
    font-size: 17px;
    letter-spacing: 0.5px;
    text-transform: uppercase;
  }
  /* Back */
  .card-back { background: var(--brand-red); }
  .back-mark {
    position: absolute;
    left: 40px; top: 180px;
    width: 250px;
    display: flex;
    align-items: center;
    gap: 12px;
    color: var(--paper);
    font-weight: 700;
    font-size: 40px;
  }
  .back-mark .dot {
    width: 22px; height: 22px;
    border-radius: 50%;
    background: var(--paper);
    flex: none;
  }
  .back-panel {
    position: absolute;
    left: 316px; top: 0; right: 0; bottom: 0;
    box-shadow: -6px 0 14px rgba(0,0,0,0.18);
  }
  .holder-name {
    position: absolute;
    left: 26px; top: 70px;
    color: var(--paper);
    font-weight: 600;
    font-size: 24px;
  }
  .holder-role {
    position: absolute;
    left: 26px; top: 102px;
    color: var(--muted);
    font-size: 15px;
  }
  .name-band {
    position: absolute;
    left: 0; right: 0; top: 128px;
    height: 112px;
    background: var(--paper);
    display: flex;
    align-items: center;
    padding-left: 26px;
    color: var(--ink);
    font-weight: 700;
    font-size: 52px;
  }
  .contact-list {
    position: absolute;
    left: 26px; top: 268px;
    list-style: none;
    color: var(--paper);
    font-size: 17px;
  }
  .contact-list li {
    display: flex;
    align-items: center;
    gap: 12px;
    height: 30px;
  }
  .contact-list svg { width: 14px; height: 14px; fill: var(--ink); flex: none; }
</style>
</head>
<body>
  <section class="card card-front">
    <div class="front-wordmark">PlateMarks</div>
    <p class="front-tagline">The definitive guide to kosher dining for the kosher consumer</p>
  </section>

  <section class="card card-back">
    <div class="back-mark"><span class="dot"></span>PlateMarks</div>
    <div class="back-panel">
      <h2 class="holder-name">Aaron Feldman</h2>
      <p class="holder-role">Director</p>
      <div class="name-band">PlateMarks</div>
      <ul class="contact-list">
        <li>
          <svg viewBox="0 0 24 24" aria-hidden="true"><path d="M6.6 10.8a15.1 15.1 0 0 0 6.6 6.6l2.2-2.2a1 1 0 0 1 1-.25 11.4 11.4 0 0 0 3.6.57 1 1 0 0 1 1 1V20a1 1 0 0 1-1 1A17 17 0 0 1 3 4a1 1 0 0 1 1-1h3.5a1 1 0 0 1 1 1c0 1.25.2 2.45.57 3.57a1 1 0 0 1-.25 1z"/></svg>
          +330 2460-1194
        </li>
        <li>
          <svg viewBox="0 0 24 24" aria-hidden="true"><path d="M2 5h20v14H2z M4 7v.5l8 5 8-5V7l-8 5z" fill-rule="evenodd"/></svg>
          info@restaurant.vintrello.com
        </li>
        <li>
          <svg viewBox="0 0 24 24" aria-hidden="true"><path d="M12 2a10 10 0 1 0 0 20 10 10 0 0 0 0-20zm0 2c1 1.3 1.8 3 2.1 5H9.9C10.2 7 11 5.3 12 4zM4.3 11h3.6c0 .7 0 1.4.1 2H4.3a8 8 0 0 1 0-2zm5.6 0h4.2v2H9.9zm6.2 0h3.6a8 8 0 0 1 0 2h-3.6c.1-.6.1-1.3 0-2zM9.9 15h4.2c-.3 2-1.1 3.7-2.1 5-1-1.3-1.8-3-2.1-5z"/></svg>
          www.restaurant.vintrello.com
        </li>
      </ul>
    </div>
  </section>
</body>
</html>
```